A website design for a consultation firm

We are located in Istanbul, Turkey and offers our consultation services to customers interested in investing in Realestate, Education and Investment particularly this coming from Arab world and English speaking countries.

The site should carry our message of deep knowledge about the Turkish markets in the mentioned sectors of interest, sincerity and keenness.

The final deliverable of the winning design should include:
- The source files of the final designs. e.g. AI, PSD ..etc
- The redline markup for the design using a Specctr or any other similar tool.

Target Market(s)

English and Arabic speaking countries with a Turkish theme since we are a Turkish company

Industry/Entity Type

Consulting

Number of Pages Required

2 page

Font styles to use
Sans Serif

Requirements
Must have
• The site should serve the following main sections:
• - Why QVE?
• - Reports & studies
• - Sectors
• - Our team
• - Contact
• We need a design that could be converted into a WordPress theme.
• The design should be in English but should accommodate other languages including RTL.
• You can use the color theme you like as long as it does't dissolve the logo.
• The site should link into our accounts on the following networks:
• - Twitter
• - Facebook
• - LinkedIn
• The design should be responsive and nicely rendered on Desktop, Tablets and Smart phones.
Nice to have
• The site would be nice to balance between being informative and

```html
<!DOCTYPE html>
<html lang="en">
<head>
<meta charset="utf-8">
<title>QVE Consulting</title>
<link href="https://fonts.googleapis.com/css2?family=Quicksand:wght@300;400;500;700&family=Lato:wght@400;700&display=swap" rel="stylesheet">
<style>
:root{
  --red:#e31b2b;
  --red-dark:#b5101d;
  --navy:#1d3566;
  --navy-deep:#1a2f5c;
  --ink:#222;
  --text:#555;
  --white:#fff;
}
*{box-sizing:border-box;margin:0;padding:0}
html,body{width:1200px;height:2387px;overflow:hidden;background:var(--white)}
body{font-family:"Lato",Arial,sans-serif;color:var(--ink);position:relative}
.page{position:relative;width:1200px;height:2387px;overflow:hidden}

/* header */
.site-header{position:absolute;left:0;top:0;width:1200px;height:122px;background:var(--white);border-top:3px solid var(--navy);box-shadow:0 4px 10px rgba(0,0,0,.15);z-index:3}
.brand{position:absolute;left:78px;top:28px;display:flex;align-items:center;gap:10px}
.brand-dot{width:20px;height:20px;border-radius:50%;background:var(--red)}
.brand-name{font-family:"Quicksand",sans-serif;font-weight:700;font-size:40px;color:var(--red);line-height:1}
.brand-sub{position:absolute;left:108px;top:72px;font-family:"Quicksand",sans-serif;font-size:18px;color:var(--navy)}
.top-mail{position:absolute;left:535px;top:12px;font-size:16px;color:var(--ink);display:flex;align-items:center;gap:10px}
.top-phone{position:absolute;left:798px;top:0;width:156px;height:40px;background:var(--navy);color:var(--white);font-size:17px;display:flex;align-items:center;justify-content:center;gap:10px}
.langs{position:absolute;left:996px;top:10px;display:flex;gap:16px}
.langs span{width:22px;height:22px;border-radius:50%;background:#c9c9c9;border:1px solid #aaa}
.langs span:first-child{background:#2b4a8c}
.main-nav{position:absolute;left:551px;top:60px;display:flex;align-items:stretch;height:67px}
.main-nav a{font-family:"Quicksand",sans-serif;font-size:16px;color:#444;text-decoration:none;padding:20px 16px 0;height:67px}
.main-nav a.active{background:var(--red);color:var(--white);width:77px;padding:20px 0 0;text-align:center;border-radius:3px 3px 0 0}

/* hero */
.hero{position:absolute;left:0;top:122px;width:1200px;height:543px;background:linear-gradient(90deg,#dfe6ee 0%,#b9c8d8 45%,#8ea4bd 100%)}
.hero-photo{position:absolute;left:550px;top:0;width:650px;height:543px;background:radial-gradient(ellipse at 55% 40%,#f3d9b0 0%,#c9b39a 18%,#5f6670 45%,#3b3f47 80%)}
.hero-title{position:absolute;left:78px;top:172px;font-family:"Quicksand",sans-serif;font-size:51px;line-height:58px;color:var(--white);font-weight:400}
.hero-title .hl{color:var(--red);font-weight:500}
.hero-title b{font-weight:700}
.btn{position:absolute;background:var(--red);color:var(--white);border-radius:26px;font-size:17px;display:flex;align-items:center;justify-content:center;gap:10px;box-shadow:0 3px 0 var(--red-dark)}
.hero-btn{left:78px;top:309px;width:186px;height:51px}
.slide-arrow{position:absolute;top:260px;width:50px;height:40px;background:var(--white);display:flex;align-items:center;justify-content:center}

/* why */
.why-art{position:absolute;left:78px;top:692px;width:359px;height:358px;border-radius:50%;background:radial-gradient(circle at 45% 45%,#f2d27a 0%,#d7a63c 55%,#c9242d 90%,transparent 91%)}
.why-title{position:absolute;left:481px;top:725px;font-family:"Quicksand",sans-serif;font-weight:700;font-size:38px;color:#111}
.why-title .n{color:var(--navy)}
.why-title small{font-size:22px;font-weight:500;color:var(--navy)}
.why-copy{position:absolute;left:481px;top:785px;width:640px;font-family:Arial,sans-serif;font-size:14px;line-height:22.5px;color:var(--text)}
.why-copy p+p{margin-top:22px}
.why-btn{left:478px;top:1003px;width:186px;height:51px}

/* sectors */
.sectors{position:absolute;left:0;top:1105px;width:1200px;height:552px;background:linear-gradient(135deg,#f3f3f3,#e6e6e6)}
.section-title{font-family:"Quicksand",sans-serif;font-size:40px;font-weight:500}
.sectors .section-title{position:absolute;left:0;width:1200px;top:46px;text-align:center;color:var(--red)}
.divider{position:absolute;left:428px;top:103px;width:344px;height:1px;background:#ccc}
.divider::after{content:"";position:absolute;left:166px;top:-5px;width:11px;height:11px;border-radius:50%;background:#bbb}
.sector-card{position:absolute;top:133px;width:333px;height:358px;background:var(--navy);border-radius:4px;box-shadow:0 2px 4px rgba(0,0,0,.25)}
.sector-card h3{height:51px;background:linear-gradient(#ef2a3a,#c81424);color:var(--white);font-weight:400;font-size:22px;text-align:center;line-height:51px;border-radius:4px 4px 0 0}
.sector-icon{position:absolute;left:104px;top:72px;width:124px;height:124px;border-radius:50%;background:var(--white);display:flex;align-items:center;justify-content:center}
.sector-card p{position:absolute;left:20px;top:220px;width:293px;text-align:center;color:var(--white);font-size:15px;line-height:25px}
.sector-more{position:absolute;left:85px;bottom:0;width:162px;height:42px;background:linear-gradient(#fff,#e4e4e4);color:var(--red-dark);font-size:16px;font-weight:700;text-align:center;line-height:44px;border-radius:10px 10px 0 0}

/* reports */
.reports-title{position:absolute;left:78px;top:1680px;font-size:37px;color:var(--navy)}
.reports-title .amp{color:#111}
.reports-title .r{color:var(--red)}
.report{position:absolute;left:78px;width:490px;height:100px}
.report-thumb{position:absolute;left:0;top:0;width:100px;height:100px;border:3px solid #ddd;background:linear-gradient(135deg,#cdd8e2,#7d8fa4)}
.report h4{position:absolute;left:121px;top:0;font-family:"Quicksand",sans-serif;font-weight:500;font-size:18px;color:#111}
.report p{position:absolute;left:121px;top:30px;width:370px;font-family:Arial,sans-serif;font-size:13.5px;line-height:22px;color:var(--text)}
.report a{position:absolute;left:121px;top:80px;font-size:14px;color:var(--red);text-decoration:none}
.view-all{position:absolute;left:78px;top:2010px;font-size:14px;color:var(--red)}

.tweets{position:absolute;left:620px;top:1687px;width:469px;height:342px;border:1px solid #ccc;background:var(--white)}
.tweets-head{height:40px;border-bottom:1px solid #ddd;display:flex;align-items:center;justify-content:space-between;padding:0 10px}
.tweets-head strong{font-size:16px}
.follow-btn{border:1px solid #ccc;border-radius:3px;padding:3px 8px;font-size:13px;font-weight:700;background:#f5f5f5}
.tweet{position:relative;height:88px;border-bottom:1px solid #e5e5e5;padding:8px 50px 0 74px;font-size:13.5px;line-height:20px}
.tweet-avatar{position:absolute;left:10px;top:12px;width:54px;height:54px;border:1px solid #ccc;display:flex;align-items:center;justify-content:center;font-family:"Quicksand",sans-serif;font-weight:700;font-size:15px;color:var(--red)}
.tweet b{font-size:14px}
.tweet .handle{color:#777}
.tweet .time{position:absolute;right:24px;top:6px;color:#888;font-size:12px}
.tweet p{color:#555}
.tweet-box{position:absolute;left:5px;bottom:6px;width:457px;height:32px;border:1px solid #ccc;font-size:13px;color:#666;padding:7px 10px}

/* footer */
.site-footer{position:absolute;left:0;top:2075px;width:1200px;height:257px;background:var(--navy-deep);border-top:5px solid var(--red);color:var(--white)}
.foot-col{position:absolute;top:36px}
.foot-col h5{font-family:"Quicksand",sans-serif;font-weight:500;font-size:19px;margin-bottom:18px}
.sitemap li{list-style:none;font-size:14px;line-height:27px;color:#b9c3d8}
.sitemap li:first-child{color:var(--white)}
.sitemap li::before{content:"» ";}
.contact-row{display:flex;gap:14px;font-size:15px;line-height:26px;margin-bottom:14px}
.contact-row svg{flex:0 0 auto;margin-top:4px}
.news-item{position:relative;height:72px;padding-left:70px;font-size:14px;line-height:20px}
.news-avatar{position:absolute;left:0;top:4px;width:54px;height:54px;border-radius:50%;background:linear-gradient(135deg,#c5ccd8,#6b7a92)}
.news-item em{display:block;font-size:12px;color:#c9d2e4}
.foot-brand{position:absolute;left:935px;top:48px;width:130px;text-align:center;font-family:"Quicksand",sans-serif;font-weight:700;font-size:34px;color:var(--white)}
.foot-brand small{display:block;font-size:16px;font-weight:500}
.foot-rule{position:absolute;left:923px;top:152px;width:147px;height:1px;background:#4a5f8a}
.socials{position:absolute;left:937px;top:167px;display:flex;gap:8px}
.socials span{width:36px;height:36px;border-radius:50%;border:2px solid var(--white)}
.socials span:first-child{background:var(--white)}
.bottom-bar{position:absolute;left:0;top:2332px;width:1200px;height:55px;background:var(--red);color:var(--white);font-family:"Quicksand",sans-serif;font-size:14px;text-align:center;line-height:55px}
</style>
</head>
<body>
<div class="page">

<header class="site-header">
  <div class="brand"><span class="brand-dot"></span><span class="brand-name">QVE</span></div>
  <div class="brand-sub">consulting</div>
  <div class="top-mail">
    <svg width="16" height="12" viewBox="0 0 16 12"><rect width="16" height="12" fill="#e31b2b"/><path d="M0 0l8 7 8-7" stroke="#fff" stroke-width="1.5" fill="none"/></svg>
    info@qveconsulting.com
  </div>
  <div class="top-phone">
    <svg width="16" height="16" viewBox="0 0 24 24"><path fill="#fff" d="M6.6 10.8a15 15 0 006.6 6.6l2.2-2.2c.3-.3.7-.4 1-.2 1.1.4 2.3.6 3.6.6.6 0 1 .4 1 1V20c0 .6-.4 1-1 1A17 17 0 013 4c0-.6.4-1 1-1h3.5c.6 0 1 .4 1 1 0 1.3.2 2.5.6 3.6.1.3 0 .7-.2 1z"/></svg>
    555 0134 200
  </div>
  <div class="langs" aria-label="Language choices"><span></span><span></span><span></span><span></span></div>
  <nav class="main-nav">
    <a class="active" href="#">Home</a><a href="#">About</a><a href="#">Report &amp; Study</a><a href="#">Sectors</a><a href="#">Our Team</a><a href="#">Contact</a>
  </nav>
</header>

<section class="hero">
  <div class="hero-photo" role="img" aria-label="Businessman in a suit holding a glowing brain above his hands"></div>
  <h1 class="hero-title">UNLOCK the <span class="hl">Turkish</span><br>Market for <b>Investors</b></h1>
  <div class="btn hero-btn">CONTACT NOW</div>
  <div class="slide-arrow" style="left:0"><svg width="22" height="16" viewBox="0 0 22 16"><path d="M0 8l10-8v5h12v6H10v5z" fill="#ccc"/></svg></div>
  <div class="slide-arrow" style="right:0"><svg width="22" height="16" viewBox="0 0 22 16"><path d="M22 8L12 0v5H0v6h12v5z" fill="#e31b2b"/></svg></div>
</section>

<section class="why">
  <div class="why-art" role="img" aria-label="Golden wireframe globe wrapped by a red arrow"></div>
  <h2 class="why-title">WHY <span class="n">QVE</span> <small>consulting</small>?</h2>
  <div class="why-copy">
    <p>Lorem Ipsum is simply dummy text of the printing and typesetting industry. Lorem Ipsum has been the industry's standard dummy text ever since the 1500s, when an unknown printer took a galley of type and scrambled it to make a type specimen book. It has survived not only five centuries, but also the leap into electronic typesetting, remaining essentially unchanged.</p>
    <p>It was popularised in the 1960s with the release of Tessera sheets containing Lorem Ipsum passages, and more recently with desktop publishing software like Pagewright Studio including versions of Lorem Ipsum.</p>
  </div>
  <div class="btn why-btn">READ MORE <svg width="14" height="12" viewBox="0 0 14 12"><path d="M1 1l5 5-5 5M7 1l5 5-5 5" stroke="#fff" stroke-width="1.6" fill="none"/></svg></div>
</section>

<section class="sectors">
  <h2 class="section-title">SECTORS</h2>
  <div class="divider"></div>

  <article class="sector-card" style="left:78px">
    <h3>REAL ESTATE</h3>
    <div class="sector-icon"><svg width="64" height="60" viewBox="0 0 64 60"><g fill="#e31b2b"><rect x="8" y="6" width="22" height="54"/><rect x="32" y="20" width="16" height="40"/><rect x="50" y="34" width="12" height="26"/></g><g fill="#fff"><rect x="12" y="12" width="5" height="5"/><rect x="21" y="12" width="5" height="5"/><rect x="12" y="22" width="5" height="5"/><rect x="21" y="22" width="5" height="5"/><rect x="12" y="32" width="5" height="5"/><rect x="21" y="32" width="5" height="5"/><rect x="36" y="26" width="8" height="4"/><rect x="36" y="36" width="8" height="4"/><rect x="53" y="40" width="6" height="4"/></g></svg></div>
    <p>Lorem Ipsum is simply dummy text of the printing and typesetting industry. Lorem Ipsum has been the industry's.</p>
    <div class="sector-more">READ MORE</div>
  </article>

  <article class="sector-card" style="left:434px">
    <h3>EDUCATION</h3>
    <div class="sector-icon"><svg width="70" height="52" viewBox="0 0 70 52"><path d="M35 2L2 18l33 16 33-16z" fill="#e31b2b"/><path d="M16 26v14c0 6 38 6 38 0V26L35 36z" fill="#e31b2b"/><path d="M62 20v18" stroke="#e31b2b" stroke-width="3"/></svg></div>
    <p>Lorem Ipsum is simply dummy text of the printing and typesetting industry. Lorem Ipsum has been the industry's.</p>
    <div class="sector-more">READ MORE</div>
  </article>

  <article class="sector-card" style="left:790px">
    <h3>INVESTMENT</h3>
    <div class="sector-icon"><svg width="64" height="62" viewBox="0 0 64 62"><text x="22" y="16" font-family="Arial" font-weight="700" font-size="18" fill="#e31b2b">$</text><g fill="#e31b2b"><rect x="6" y="42" width="9" height="18"/><rect x="19" y="36" width="9" height="24"/><rect x="32" y="40" width="9" height="20"/><rect x="45" y="28" width="9" height="32"/></g><path d="M4 36l14-10 12 8 20-16" stroke="#e31b2b" stroke-width="3" fill="none"/><path d="M44 14h10v10z" fill="#e31b2b"/></svg></div>
    <p>Lorem Ipsum is simply dummy text of the printing and typesetting industry. Lorem Ipsum has been the industry's.</p>
    <div class="sector-more">READ MORE</div>
  </article>
</section>

<section class="reports">
  <h2 class="section-title reports-title">REPORTS <span class="amp">&amp;</span> <span class="r">STUDIES</span></h2>
  <div class="report" style="top:1741px">
    <div class="report-thumb" role="img" aria-label="Business people working at an office desk"></div>
    <h4>Lorem Ipsum is simply dumm</h4>
    <p>Lorem Ipsum is simply dummy text of the printing and typesetting industry. Lorem Ipsum has been the</p>
    <a href="#">LEARN MORE</a>
  </div>
  <div class="report" style="top:1855px">
    <div class="report-thumb" role="img" aria-label="Business people working at an office desk"></div>
    <h4>Lorem Ipsum is simply dumm</h4>
    <p>Lorem Ipsum is simply dummy text of the printing and typesetting industry. Lorem Ipsum has been the</p>
    <a href="#">LEARN MORE</a>
  </div>
  <div class="view-all">VIEW ALL</div>

  <aside class="tweets">
    <div class="tweets-head"><strong>Tweets</strong><span class="follow-btn">Follow@qveconsulting</span></div>
    <div class="tweet"><div class="tweet-avatar">QVE</div><span class="time">18h</span><b>QVE Consulting</b> <span class="handle">@qveconsulting</span><p>Lorem Ipsum is simply dummy text of the printing and type setting industry. Lorem Ipsum has been the</p></div>
    <div class="tweet"><div class="tweet-avatar">QVE</div><span class="time">9h</span><b>QVE Consulting</b> <span class="handle">@qveconsulting</span><p>Lorem Ipsum is simply dummy text of the printing and type setting industry. Lorem Ipsum has been the</p></div>
    <div class="tweet"><div class="tweet-avatar">QVE</div><span class="time">9h</span><b>QVE Consulting</b> <span class="handle">@qveconsulting</span><p>Lorem Ipsum is simply dummy text of the printing and type setting industry. Lorem Ipsum has been the</p></div>
    <div class="tweet-box">Tweet to @qveconsulting</div>
  </aside>
</section>

<footer class="site-footer">
  <div class="foot-col" style="left:78px">
    <h5>SITEMAP</h5>
    <ul class="sitemap"><li>Home</li><li>About</li><li>Report &amp; Study</li><li>Sectors</li><li>Our Team</li><li>Contact</li></ul>
  </div>
  <div class="foot-col" style="left:345px;width:230px">
    <h5>CONTACT INFO</h5>
    <div class="contact-row"><svg width="16" height="20" viewBox="0 0 16 20"><path d="M8 0a8 8 0 00-8 8c0 6 8 12 8 12s8-6 8-12a8 8 0 00-8-8zm0 11a3 3 0 110-6 3 3 0 010 6z" fill="#fff"/></svg><span>123 Building Name, Street, City, Country - Zip code</span></div>
    <div class="contact-row"><svg width="18" height="18" viewBox="0 0 24 24"><path fill="#fff" d="M6.6 10.8a15 15 0 006.6 6.6l2.2-2.2c.3-.3.7-.4 1-.2 1.1.4 2.3.6 3.6.6.6 0 1 .4 1 1V20c0 .6-.4 1-1 1A17 17 0 013 4c0-.6.4-1 1-1h3.5c.6 0 1 .4 1 1 0 1.3.2 2.5.6 3.6.1.3 0 .7-.2 1z"/></svg><span>01 5550 1234</span></div>
    <div class="contact-row"><svg width="18" height="14" viewBox="0 0 18 14"><rect width="18" height="14" rx="1" fill="#fff"/><path d="M0 1l9 7 9-7" stroke="#1a2f5c" stroke-width="1.5" fill="none"/></svg><span>info@qveconsulting.com</span></div>
  </div>
  <div class="foot-col" style="left:609px;width:240px">
    <h5>NEWS</h5>
    <div class="news-item"><div class="news-avatar" role="img" aria-label="News author portrait"></div>Lorem Ipsum is simply dummy text of the.<em>12th June, 2016</em></div>
    <div class="news-item"><div class="news-avatar" role="img" aria-label="News author portrait"></div>Lorem Ipsum is simply dummy text of the.<em>12th June, 2016</em></div>
  </div>
  <div class="foot-brand">QVE<small>consulting</small></div>
  <div class="foot-rule"></div>
  <div class="socials"><span aria-label="Social profile one"></span><span aria-label="Social profile two"></span><span aria-label="Social profile three"></span></div>
</footer>
<div class="bottom-bar">© QVE consulting - 2016. All Rights Reserved.</div>

</div>
</body>
</html>
```